Awesome Business Card Design needed!

Hey there.
I'm looking for a simple but awesome business card design.
Type of company: Online advertisement agency
(please don't use the typical business people or statistics images on the card)
The front has to display the business name
and possibly some sort of logo ( perhaps something with the two M's of the biz name )
And the back of the card should say:
Name
Phone
Email
Let your imagination flow.
here are some designs that I like and that you can use as inspiration.
Simple but Awesome
http://images.pixelvantor.net/designs/55128_877673_43091_thumbnail.jpg
http://images.pixelvantor.net/designs/37714_747642_40106_image.jpg
http://images.pixelvantor.net/designs/55128_877673_43091_image.jpg
http://images.pixelvantor.net/designs/51321_781878_43091_image.jpg
http://images.pixelvantor.net/designs/33378_399063_15912_image.jpg
http://images.pixelvantor.net/designs/2337_271604_9495_image.jpg
good luck

```html
<!DOCTYPE html>
<html lang="en">
<head>
<meta charset="utf-8">
<title>halvern media – business card</title>
<link rel="stylesheet" href="https://fonts.googleapis.com/css2?family=Arimo&display=swap">
<style>
  :root {
    --page: #ffffff;
    --card-edge: #5a5a5a;
    --band-light: #f4f4f4;
    --band-dark: #d0d0d0;
    --divider: #3c3c3c;
    --brand: #6f9aa6;
    --mark: #3d7a6d;
    --ink: #222222;
  }
  html, body {
    margin: 0;
    padding: 0;
    width: 932px;
    height: 1200px;
    overflow: hidden;
    background: var(--page);
  }
  .canvas {
    position: relative;
    width: 932px;
    height: 1200px;
  }
  .card {
    position: absolute;
    left: 16px;
    width: 903px;
    box-sizing: border-box;
    border: 1.5px solid var(--card-edge);
    background: var(--page);
  }
  .card--front { top: 13px; height: 582px; }
  .card--back { top: 606px; height: 587px; }

  .band {
    position: absolute;
    background: linear-gradient(to right, rgba(208, 208, 208, 0) 0%, var(--band-light) 15%, var(--band-dark) 100%);
  }
  .card--front .band { left: 46px; top: 18px; width: 852px; height: 186px; }
  .card--back .band { left: 46px; top: 11px; width: 840px; height: 186px; }

  .divider {
    position: absolute;
    left: 566px;
    top: 0;
    width: 1.5px;
    height: 390px;
    background: var(--divider);
  }
  .brand {
    position: absolute;
    right: 350px;
    top: 318px;
    margin: 0;
    font-family: "Arimo", Arial, sans-serif;
    font-weight: 400;
    font-size: 40px;
    line-height: 48px;
    white-space: nowrap;
    color: var(--brand);
  }
  .brand-square {
    position: absolute;
    left: 596px;
    top: 298px;
    width: 88px;
    height: 88px;
    background: var(--mark);
  }
  .contact {
    position: absolute;
    left: 112px;
    top: 285px;
    margin: 0;
    padding: 0;
    list-style: none;
    font-family: "Arimo", Arial, sans-serif;
    font-size: 27px;
    color: var(--ink);
  }
  .contact li {
    height: 72px;
    line-height: 36px;
  }
</style>
</head>
<body>
<main class="canvas">
  <section class="card card--front" aria-label="Card front">
    <div class="band" role="img" aria-label="Grey horizontal stripe band fading in from the left"></div>
    <div class="divider"></div>
    <h1 class="brand">halvern media</h1>
    <div class="brand-square" aria-hidden="true"></div>
  </section>

  <section class="card card--back" aria-label="Card back">
    <div class="band" role="img" aria-label="Grey horizontal stripe band fading in from the left"></div>
    <ul class="contact">
      <li class="contact-name">name</li>
      <li class="contact-phone">phone</li>
      <li class="contact-email">email</li>
    </ul>
  </section>
</main>
</body>
</html>
```